Business Cards for Communications Technology Company

We are an innovative software company based in Tropical North Queensland, Australia. We have several brands with a focus on communications software for businesses. We are looking for a business card that is very innovate and creative whilst still remaining professional on a corporate level.

Our internal culture is very progressive and expresses a blend between the clarity of our natural surroundings and the highly technological industry we work in. Our current branding blends a modern minimalist typeface with the desire to push the boundaries in the way we communicate.

This is a corporate level business card for the communications software industry and may possibly also encompass our brands MarNetwork, PelFax, TukMailer and our B2B marketing service—with our companies name being Viresca Partners. Showing other brands on the business card is optional not compulsory.

Technical notes:

-We will attach all logo's and some examples of our corporate branding
- Would be willing to print with various papers, embossed, metallic ink, curved edges etc. in a standard business card size

Sample content:

Rowan Pellick
Senior Account Manager
Phone: 1300 842 916 / +617 4583 2764
Email: r.pellick@viresca.com.au
Web: www.viresca.com.au

Sincerely,
Viresca Partners.

```html
<!DOCTYPE html>
<html lang="en">
<head>
<meta charset="utf-8">
<title>Viresca Partners – Business Card</title>
<link rel="stylesheet" href="https://fonts.googleapis.com/css2?family=Roboto:wght@400;500;700&family=Roboto+Condensed:wght@700&display=swap">
<style>
  :root {
    --backdrop: #2a2a2c;
    --card: #141414;
    --silver: #9a9a9c;
    --silver-light: #b8b8ba;
    --silver-dim: #7c7c7e;
    --accent: #7dbb2e;
  }
  * { margin: 0; padding: 0; box-sizing: border-box; }
  html, body {
    width: 1200px; height: 900px; overflow: hidden;
    background: var(--backdrop);
    font-family: "Roboto", Arial, sans-serif;
  }
  .canvas {
    position: relative; width: 1200px; height: 900px;
  }
  .card {
    position: absolute; left: 280px; width: 640px; height: 366px;
    background: var(--card);
    box-shadow: 0 14px 34px rgba(0,0,0,.5);
  }
  .card--front { top: 52px; }
  .card--back { top: 478px; }

  .brand {
    position: absolute; inset: 0;
    display: flex; align-items: center; justify-content: center; gap: 16px;
  }
  .brand__dot {
    width: 30px; height: 30px; border-radius: 50%;
    background: var(--accent);
  }
  .brand__name {
    font-weight: 500; font-size: 38px; letter-spacing: 1px;
    color: var(--silver-light);
  }

  .identity {
    position: absolute; left: 60px; top: 128px; width: 262px; text-align: right;
  }
  .identity__name {
    font-family: "Roboto Condensed", "Arial Narrow", sans-serif;
    font-weight: 700; font-size: 40px; letter-spacing: 1.5px;
    text-transform: uppercase; color: var(--silver); line-height: 1;
  }
  .identity__title {
    margin-top: 8px; font-size: 17px; font-weight: 500; color: var(--silver-dim);
  }
  .divider {
    position: absolute; left: 344px; top: 118px; width: 2px; height: 100px;
    background: var(--silver-dim);
  }
  .contacts {
    position: absolute; left: 370px; top: 118px; list-style: none;
  }
  .contacts li {
    display: flex; align-items: center; gap: 14px;
    height: 25px; font-size: 16px; letter-spacing: .8px; color: var(--silver);
  }
  .contacts svg { width: 14px; height: 14px; flex: none; }
  .products {
    position: absolute; left: 0; right: 0; top: 282px;
    display: flex; justify-content: center; gap: 34px;
  }
  .products span {
    font-weight: 700; font-size: 23px; color: var(--silver-dim);
  }
</style>
</head>
<body>
<main class="canvas">
  <section class="card card--front" aria-label="Card front">
    <div class="brand">
      <span class="brand__dot"></span>
      <span class="brand__name">Viresca Partners</span>
    </div>
  </section>

  <section class="card card--back" aria-label="Card back">
    <div class="identity">
      <p class="identity__name">Rowan Pellick</p>
      <p class="identity__title">Senior Account Manager</p>
    </div>
    <div class="divider"></div>
    <ul class="contacts">
      <li>
        <svg viewBox="0 0 16 16" fill="none" stroke="#7c7c7e" stroke-width="1.6"><path d="M4 1.5l2.5 3-1.5 1.8c.8 1.8 2 3 3.8 3.8l1.8-1.5 3 2.5-1.6 2.4C7 13.5 2.5 9 1.6 3.1z"/></svg>
        1300 842 916
      </li>
      <li>
        <svg viewBox="0 0 16 16" fill="none" stroke="#7c7c7e" stroke-width="1.6"><rect x="4" y="1" width="8" height="14" rx="1.5"/><path d="M7 12.5h2"/></svg>
        +617 4583 2764
      </li>
      <li>
        <svg viewBox="0 0 16 16" fill="none" stroke="#7c7c7e" stroke-width="1.6"><rect x="1" y="3" width="14" height="10"/><path d="M1 3l7 6 7-6"/></svg>
        r.pellick@viresca.com.au
      </li>
      <li>
        <svg viewBox="0 0 16 16" fill="none" stroke="#7c7c7e" stroke-width="1.4"><circle cx="8" cy="8" r="6.5"/><path d="M1.5 8h13M8 1.5c-3 3.5-3 9.5 0 13M8 1.5c3 3.5 3 9.5 0 13"/></svg>
        www.viresca.com.au
      </li>
    </ul>
    <div class="products">
      <span>MarNetwork</span>
      <span>TukMailer</span>
      <span>PelFax</span>
    </div>
  </section>
</main>
</body>
</html>
```